Award-winnning Estate Agent needs a premium version of their 'For Sale' board design

We need a premium option for our 'For Sale' board design. We have a standard board that is attached to this brief, but were are looking to have a premium design version that we will use when selling exclusive properties. Our company name is Harbourline Row Estates and the name for this is exclusive selection is: 'The Harbourline Portfolio'. The design needs to work with our current brand, but have a distinctive PREMIUM feel to it. I have uploaded the barnd guidelines and also some of the exisisting logo variations. We do NOT need a new logo but feel free to play around with colours, fonts, sizes etc. for the sign.

Target Market(s)

Property buyers & house hunters

Industry/Entity Type

Real Estate - Residential Property

Font styles to use
Sans Serif

Requirements
Must have
• A premium fee, must be square design, must be easy to read when driving past the sign
Nice to have
• I'm open ot ideas

```html
<!DOCTYPE html>
<html lang="en">
<head>
<meta charset="utf-8">
<title>Harbourline Row Estates – The Harbourline Portfolio For Sale Board</title>
<link href="https://fonts.googleapis.com/css2?family=Montserrat:wght@400;600;700;800&display=swap" rel="stylesheet">
<style>
  :root {
    --backdrop: #dcdde0;
    --board-white: #ffffff;
    --brand-purple: #3d2f73;
    --roof-purple: #432f78;
    --sale-blue: #32509b;
    --phone-band: #40306f;
    --web-band: #2b3583;
    --sky-blue: #4a9fd6;
    --premium-gold: #b08d3c;
    --text-light: #ffffff;
  }
  * { margin: 0; padding: 0; box-sizing: border-box; }
  html, body {
    width: 900px; height: 1200px; overflow: hidden;
    background: var(--backdrop);
  }
  .canvas { position: relative; width: 900px; height: 1200px; }
  .board {
    position: absolute; left: 60px; top: 210px;
    width: 780px; height: 780px;
    background: var(--board-white);
    box-shadow: 4px 5px 10px rgba(0,0,0,0.22);
    overflow: hidden;
    font-family: 'Montserrat', sans-serif;
  }
  .board-shapes { position: absolute; inset: 0; }
  .sale-texture {
    position: absolute; left: 0; top: 218px;
    width: 780px; height: 382px;
    background: linear-gradient(180deg, rgba(255,255,255,0.05), rgba(0,0,0,0.06));
    clip-path: polygon(0 100px, 390px 0, 780px 100px, 780px 382px, 0 382px);
  }
  .brand-mark {
    position: absolute; left: 50%; top: 40px;
    width: 36px; height: 36px; margin-left: -18px;
    background: var(--sky-blue);
  }
  .brand-name {
    position: absolute; left: 0; right: 0; top: 92px;
    text-align: center;
    font-weight: 700; font-size: 36px; line-height: 1;
    color: var(--brand-purple);
    letter-spacing: -0.5px;
  }
  .collection-name {
    position: absolute; left: 0; right: 0; top: 144px;
    display: flex; justify-content: center; align-items: center; gap: 16px;
    font-weight: 600; font-size: 17px; line-height: 1;
    letter-spacing: 5px; text-transform: uppercase;
    color: var(--premium-gold);
  }
  .collection-name::before,
  .collection-name::after {
    content: ""; width: 60px; height: 2px; background: var(--premium-gold);
  }
  .headline {
    position: absolute; left: 0; right: 0;
    text-align: center; color: var(--text-light);
    font-weight: 800; font-size: 128px; line-height: 1;
    text-shadow: 3px 4px 5px rgba(0,0,0,0.35);
  }
  .headline-for { top: 290px; }
  .headline-sale { top: 432px; }
  .phone {
    position: absolute; left: 0; right: 0; top: 614px;
    text-align: center; color: var(--text-light);
    font-weight: 800; font-size: 72px; line-height: 1;
    letter-spacing: 1px;
  }
  .web {
    position: absolute; left: 0; right: 0; top: 727px;
    text-align: center; color: var(--text-light);
    font-weight: 400; font-size: 26px; line-height: 1;
    letter-spacing: 2px;
  }
</style>
</head>
<body>
<main class="canvas">
  <section class="board">
    <svg class="board-shapes" width="780" height="780" viewBox="0 0 780 780" aria-hidden="true">
      <polygon points="0,300 390,200 780,300 780,600 0,600" fill="var(--roof-purple)"/>
      <polygon points="0,318 390,218 780,318 780,600 0,600" fill="var(--sale-blue)"/>
      <rect x="0" y="600" width="780" height="100" fill="var(--phone-band)"/>
      <rect x="0" y="700" width="780" height="80" fill="var(--web-band)"/>
      <rect x="12" y="12" width="756" height="756" fill="none" stroke="var(--premium-gold)" stroke-width="2"/>
    </svg>
    <div class="sale-texture" role="img" aria-label="Subtle geometric lattice pattern across the blue sale panel"></div>
    <div class="brand-mark"></div>
    <p class="brand-name">Harbourline Row Estates</p>
    <p class="collection-name">The Harbourline Portfolio</p>
    <h1 class="headline headline-for">FOR</h1>
    <h1 class="headline headline-sale">SALE</h1>
    <p class="phone">01632 960418</p>
    <p class="web">www.harbourlinerowestates.co.uk</p>
  </section>
</main>
</body>
</html>
```